Etiketten für Gummibärchenglas
Zielgruppe
Wir sind Arbeitgeber für Pflegeberufe und bieten Arbeitsmodelle, die den Pflegeberuf erträglicher gestalten die Mitarbeiter entlasten und besser bezahlen!
Aufgabenstellung
Unseren Bewerbern sagen wir immer....'bevor Sie sich entscheiden hören Sie auf Ihr Bauchgefühl...! ' Wenn dieses komische Signale sendet, lassen Sie lieber die Finger davon!'
Nun haben wir uns überlegt, unseren Bewerbern zum Abschied aus dem Vorstellungsgespräch ein kleines 'Einmachglas' als Geschenk mitzugeben wo nur grüne Gummibärchen darin sind und ein super ansprechenden Etikett darauf ist mit einem Satz wie z.B.: K7-VITANOR....für ein gutes Bauchgefühl.
Dieses Etikett soll selbstverständlich optisch hochwertig, witzig oder ansprechend sein. Idealerweise alles zusammen! ;)
Unsere Logos/Farben und sonstiges finden Sie unter www.dienstwerk-9.de oder auf unserer Facebook-Seite: https://www.sozialnetz-beispiel.de/DienstwerkNeun/?ref=bookmarks
hier sind die Gläser die etikettiert werden sollen: https://www.kaufhafen-online.de/dp/X00Q41ZTRA/ref=kh_5172093_296851202_QX_item

```html
<!DOCTYPE html>
<html lang="de">
<head>
<meta charset="utf-8">
<title>Etikett – Für ein gutes Bauchgefühl</title>
<link rel="stylesheet" href="https://fonts.googleapis.com/css2?family=Caveat:wght@500;700&family=Open+Sans:wght@600&display=swap">
<style>
  :root {
    --page-bg: #eef0ea;
    --label-white: #ffffff;
    --label-edge: #dcdfd6;
    --brand-green: #5aa65a;
    --ink-dark: #1e1e1e;
    --figure-green: #3f9a4a;
    --figure-light: #e9efe6;
  }
  * { margin: 0; padding: 0; box-sizing: border-box; }
  html, body {
    width: 1200px;
    height: 1200px;
    overflow: hidden;
    background: var(--page-bg);
  }
  .canvas {
    position: relative;
    width: 1200px;
    height: 1200px;
  }
  .label {
    position: absolute;
    left: 100px;
    top: 100px;
    width: 1000px;
    height: 1000px;
    border-radius: 50%;
    background: var(--label-white);
    box-shadow: 0 0 0 2px var(--label-edge);
  }
  .brand {
    position: absolute;
    top: 140px;
    left: 220px;
    display: flex;
    align-items: center;
    gap: 16px;
  }
  .brand-dot {
    width: 100px;
    height: 100px;
    border-radius: 50%;
    background: var(--brand-green);
  }
  .brand-name {
    font-family: "Open Sans", Arial, sans-serif;
    font-weight: 600;
    font-size: 40px;
    letter-spacing: 1px;
    color: var(--brand-green);
  }
  .mascot {
    position: absolute;
    left: 140px;
    top: 320px;
    width: 240px;
    height: 530px;
    border-radius: 120px 120px 30px 30px;
    background: linear-gradient(180deg, var(--figure-light) 0%, var(--figure-light) 36%, var(--figure-green) 36%, var(--figure-green) 74%, var(--figure-light) 74%);
  }
  .tagline {
    position: absolute;
    inset: 0;
    width: 1000px;
    height: 1000px;
  }
  .tagline-lead {
    font-family: "Caveat", "Comic Sans MS", cursive;
    font-weight: 500;
    font-size: 66px;
    fill: var(--ink-dark);
  }
  .tagline-main {
    font-family: "Caveat", "Comic Sans MS", cursive;
    font-weight: 700;
    font-size: 124px;
    fill: var(--ink-dark);
  }
</style>
</head>
<body>
  <main class="canvas">
    <section class="label">
      <header class="brand">
        <span class="brand-dot"></span>
        <span class="brand-name">Dienstwerk Neun</span>
      </header>

      <div class="mascot" role="img" aria-label="Gezeichnete Figur in grünem Shirt, die sich zufrieden den Bauch hält"></div>

      <svg class="tagline" viewBox="0 0 1000 1000">
        <defs>
          <path id="lead-curve" d="M 420 700 Q 570 620 590 380"/>
          <path id="main-curve" d="M 410 850 Q 700 750 740 200"/>
        </defs>
        <text class="tagline-lead"><textPath href="#lead-curve">Für ein gutes</textPath></text>
        <text class="tagline-main"><textPath href="#main-curve">Bauchgefühl</textPath></text>
      </svg>
    </section>
  </main>
</body>
</html>
```